VARSEK MOBILE APP RE-DESIGN - MINIMALISTIC AND CLEAN DESIGN

We are looking for a design that is minimalistic, clean, modern and appealing to millennials...
IMPORTANT: This is NOT a logo design nor a website design... This is for a mobile App Design. You can download our app on iOS or Android: "VARSEK eLINKUP"

We are attaching our new logo and some apps that we like the design, colors, shadows, 3d effects, style, etc...

For content, you can check our website: www.varsek-app.example

Please feel free to ask questions, it's very important that you understand the project. Thank you

Also, check out this website...we do like the design and colors: https://brontil-demo.example/
Updates

This is not for a logo design... this is for a mobile app design.... please download our app on iOS: VARSEK eLINKUP... THANK YOU

Target Market(s)

20 - 35
60% Male 40 Female

Requirements
Must have
• great graphics, color shadows for 3d effects, great colors with transparency, IMPORTANT: CLEAN DESIGN, Minimalistic.

```html
<!DOCTYPE html>
<html lang="en">
<head>
<meta charset="utf-8">
<title>VARSEK – Home</title>
<link href="https://fonts.googleapis.com/css2?family=Roboto:wght@400;500&display=swap" rel="stylesheet">
<style>
  :root{
    --page-bg:#e9edf5;
    --screen-top:#cfcbe9;
    --screen-bottom:#b4e6f6;
    --ink:#1f1f24;
    --muted:#6f6f78;
    --placeholder:#8a8a99;
    --accent:#5340e6;
    --star:#f5b301;
    --star-off:#b9b9c2;
    --card:rgba(255,255,255,0.72);
    --search:rgba(255,255,255,0.55);
    --lodge:#ff5a5f;
    --seat:#00cc00;
    --crate:#26b8b8;
    --nav-ink:#6a6a72;
  }
  *{box-sizing:border-box;margin:0;padding:0}
  html,body{width:1200px;height:1200px;overflow:hidden}
  body{background:var(--page-bg);font-family:"Roboto",sans-serif;color:var(--ink)}
  .screen{
    position:absolute;left:330px;top:15px;width:540px;height:1171px;
    border-radius:44px;overflow:hidden;
    background:linear-gradient(180deg,var(--screen-top) 40%,var(--screen-bottom) 100%);
    box-shadow:0 20px 50px rgba(40,50,120,0.18);
  }
  .hero{
    position:absolute;left:0;top:0;width:540px;height:470px;
    background:linear-gradient(160deg,#8c7870 0%,#a48f84 30%,#b9a8a0 55%,#8f86b8 80%,#a7a0d8 100%);
  }
  .hero-wave{position:absolute;left:0;top:380px;width:540px;height:110px}
  .status-time{position:absolute;left:46px;top:20px;color:#fff;font-weight:500;font-size:21px}
  .search{
    position:absolute;left:32px;top:487px;width:477px;height:69px;
    background:var(--search);border-radius:3px;display:flex;align-items:center;padding-left:26px;
    box-shadow:0 2px 8px rgba(80,80,150,0.08);
  }
  .search svg{width:24px;height:24px;margin-right:28px}
  .search span{font-size:19px;color:var(--placeholder)}
  .section-title{position:absolute;left:31px;top:591px;font-size:17px;font-weight:500;letter-spacing:.3px}
  .card{
    position:absolute;left:32px;width:477px;height:122px;background:var(--card);
    border-radius:3px;display:flex;overflow:hidden;box-shadow:0 4px 12px rgba(80,90,170,0.12);
  }
  .card-brand{width:111px;height:100%;display:flex;align-items:center;justify-content:center;font-weight:500;font-size:17px}
  .brand-crate{background:#fff;color:var(--crate)}
  .brand-lodge{background:var(--lodge);color:#fff}
  .brand-seat{background:var(--seat);color:#fff}
  .brand-blank{background:#fff}
  .card-body{position:relative;flex:1;padding:14px 16px 0 24px}
  .card-title{font-size:21px;font-weight:500;line-height:1.2}
  .rating{display:flex;align-items:center;margin-top:9px;gap:6px}
  .rating svg{width:17px;height:17px}
  .rating .count{font-size:16px;color:var(--muted);margin-left:6px}
  .meta{position:absolute;left:24px;right:16px;top:86px;display:flex;align-items:center;font-size:15px}
  .meta .num{color:var(--muted);margin-right:12px}
  .badge{background:var(--accent);color:#fff;font-size:11.5px;padding:3px 12px;border-radius:9px}
  .author{margin-left:auto;font-size:13.5px;color:#444}
  .tabbar{
    position:absolute;left:0;top:1088px;width:540px;height:83px;background:#fff;
    display:flex;justify-content:space-around;padding:10px 14px 0;
  }
  .tab{display:flex;flex-direction:column;align-items:center;width:90px;font-size:16.5px;color:var(--nav-ink)}
  .tab svg{width:32px;height:32px;margin-bottom:6px}
  .tab.active{color:var(--accent)}
</style>
</head>
<body>
<main class="screen">
  <div class="hero" role="img" aria-label="Photo of a young woman holding a payment card while shopping on a laptop"></div>
  <svg class="hero-wave" viewBox="0 0 540 110" preserveAspectRatio="none" aria-hidden="true">
    <path d="M0 30 C90 0 170 40 260 25 C350 10 430 45 540 20 L540 110 L0 110Z" fill="#a79fe0" opacity=".55"/>
    <path d="M0 45 C120 25 200 70 300 55 C400 40 470 60 540 50 L540 110 L0 110Z" fill="#bcb6e8" opacity=".8"/>
    <path d="M0 75 C130 60 260 95 540 80 L540 110 L0 110Z" fill="#cbc8ea"/>
  </svg>
  <div class="status-time">9:41</div>

  <div class="search">
    <svg viewBox="0 0 24 24" fill="none" stroke="#555" stroke-width="1.8"><circle cx="10" cy="10" r="7"/><path d="M15 15l7 7"/></svg>
    <span>Search Products / Services</span>
  </div>

  <h2 class="section-title">FEATURED LISTING</h2>

  <article class="card" style="top:636px">
    <div class="card-brand brand-crate">Crate Market</div>
    <div class="card-body">
      <h3 class="card-title">$15 off on 1st order</h3>
      <div class="rating">
        <svg viewBox="0 0 24 24"><path fill="var(--star)" d="M12 2l3 7 7.5.6-5.7 4.9 1.8 7.4L12 18l-6.6 3.9 1.8-7.4L1.5 9.6 9 9z"/></svg>
        <svg viewBox="0 0 24 24"><path fill="var(--star)" d="M12 2l3 7 7.5.6-5.7 4.9 1.8 7.4L12 18l-6.6 3.9 1.8-7.4L1.5 9.6 9 9z"/></svg>
        <svg viewBox="0 0 24 24"><path fill="var(--star)" d="M12 2l3 7 7.5.6-5.7 4.9 1.8 7.4L12 18l-6.6 3.9 1.8-7.4L1.5 9.6 9 9z"/></svg>
        <svg viewBox="0 0 24 24"><path fill="var(--star)" d="M12 2l3 7 7.5.6-5.7 4.9 1.8 7.4L12 18l-6.6 3.9 1.8-7.4L1.5 9.6 9 9z"/></svg>
        <svg viewBox="0 0 24 24"><path fill="var(--star-off)" d="M12 2l3 7 7.5.6-5.7 4.9 1.8 7.4L12 18l-6.6 3.9 1.8-7.4L1.5 9.6 9 9z"/></svg>
        <span class="count">(2)</span>
      </div>
      <div class="meta"><span class="num">0</span><span class="badge">Featured</span><span class="author">By:- Mateo Rivas</span></div>
    </div>
  </article>

  <article class="card" style="top:770px">
    <div class="card-brand brand-lodge">Lodgely</div>
    <div class="card-body">
      <h3 class="card-title">Lorem ipsum dolor sit amet</h3>
      <div class="rating">
        <svg viewBox="0 0 24 24"><path fill="var(--star)" d="M12 2l3 7 7.5.6-5.7 4.9 1.8 7.4L12 18l-6.6 3.9 1.8-7.4L1.5 9.6 9 9z"/></svg>
        <svg viewBox="0 0 24 24"><path fill="var(--star)" d="M12 2l3 7 7.5.6-5.7 4.9 1.8 7.4L12 18l-6.6 3.9 1.8-7.4L1.5 9.6 9 9z"/></svg>
        <svg viewBox="0 0 24 24"><path fill="var(--star)" d="M12 2l3 7 7.5.6-5.7 4.9 1.8 7.4L12 18l-6.6 3.9 1.8-7.4L1.5 9.6 9 9z"/></svg>
        <svg viewBox="0 0 24 24"><path fill="var(--star)" d="M12 2l3 7 7.5.6-5.7 4.9 1.8 7.4L12 18l-6.6 3.9 1.8-7.4L1.5 9.6 9 9z"/></svg>
        <svg viewBox="0 0 24 24"><path fill="var(--star-off)" d="M12 2l3 7 7.5.6-5.7 4.9 1.8 7.4L12 18l-6.6 3.9 1.8-7.4L1.5 9.6 9 9z"/></svg>
        <span class="count">(2)</span>
      </div>
      <div class="meta"><span class="num">0</span><span class="badge">Featured</span><span class="author">By:- Mateo Rivas</span></div>
    </div>
  </article>

  <article class="card" style="top:905px">
    <div class="card-brand brand-seat">Seatrun</div>
    <div class="card-body">
      <h3 class="card-title">Etiam vitae eros efficitur</h3>
      <div class="rating">
        <svg viewBox="0 0 24 24"><path fill="var(--star)" d="M12 2l3 7 7.5.6-5.7 4.9 1.8 7.4L12 18l-6.6 3.9 1.8-7.4L1.5 9.6 9 9z"/></svg>
        <svg viewBox="0 0 24 24"><path fill="var(--star)" d="M12 2l3 7 7.5.6-5.7 4.9 1.8 7.4L12 18l-6.6 3.9 1.8-7.4L1.5 9.6 9 9z"/></svg>
        <svg viewBox="0 0 24 24"><path fill="var(--star)" d="M12 2l3 7 7.5.6-5.7 4.9 1.8 7.4L12 18l-6.6 3.9 1.8-7.4L1.5 9.6 9 9z"/></svg>
        <svg viewBox="0 0 24 24"><path fill="var(--star)" d="M12 2l3 7 7.5.6-5.7 4.9 1.8 7.4L12 18l-6.6 3.9 1.8-7.4L1.5 9.6 9 9z"/></svg>
        <svg viewBox="0 0 24 24"><path fill="var(--star-off)" d="M12 2l3 7 7.5.6-5.7 4.9 1.8 7.4L12 18l-6.6 3.9 1.8-7.4L1.5 9.6 9 9z"/></svg>
        <span class="count">(2)</span>
      </div>
      <div class="meta"><span class="num">0</span><span class="badge">Featured</span><span class="author">By:- Mateo Rivas</span></div>
    </div>
  </article>

  <article class="card" style="top:1039px">
    <div class="card-brand brand-blank"></div>
    <div class="card-body">
      <h3 class="card-title">Integer facilisis massa dolor</h3>
    </div>
  </article>

  <nav class="tabbar">
    <div class="tab active">
      <svg viewBox="0 0 32 32" fill="none" stroke="currentColor" stroke-width="2" stroke-linejoin="round"><path d="M4 15L16 4l12 11M7 13v15h7v-8h4v8h7V13"/></svg>Home
    </div>
    <div class="tab">
      <svg viewBox="0 0 32 32" fill="none" stroke="currentColor" stroke-width="2"><path d="M6 10h20v19H6z"/><path d="M11 13V7a5 5 0 0 1 10 0v6"/></svg>Explore
    </div>
    <div class="tab">
      <svg viewBox="0 0 32 32"><circle cx="16" cy="16" r="11" fill="#3a56d6"/></svg>Varsek
    </div>
    <div class="tab">
      <svg viewBox="0 0 32 32" fill="none" stroke="currentColor" stroke-width="2"><rect x="3" y="8" width="26" height="17"/><path d="M3 8l13 10 13-10"/></svg>Inbox
    </div>
    <div class="tab">
      <svg viewBox="0 0 32 32" fill="none" stroke="currentColor" stroke-width="2"><circle cx="16" cy="16" r="12"/><circle cx="11" cy="16" r="1.3" fill="currentColor"/><circle cx="16" cy="16" r="1.3" fill="currentColor"/><circle cx="21" cy="16" r="1.3" fill="currentColor"/></svg>More
    </div>
  </nav>
</main>
</body>
</html>
```